Verelto Services

Double sided business cards with color on front and black and white on back. I have basic ideas and graphics, but am looking for someone to take them to the next level

```html
<!DOCTYPE html>
<html lang="en">
<head>
<meta charset="utf-8">
<title>Verelto Services – Business Cards</title>
<link href="https://fonts.googleapis.com/css2?family=Michroma&display=swap" rel="stylesheet">
<style>
  :root {
    --backdrop: #dcdddc;
    --card-dark: #0d0d0d;
    --card-light: #f7f7f5;
    --ink-dark: #1a1a1a;
    --ink-light: #ffffff;
    --shadow: rgba(0, 0, 0, 0.18);
  }
  html, body {
    margin: 0;
    padding: 0;
    overflow: hidden;
  }
  body {
    width: 1200px;
    height: 1050px;
    background: var(--backdrop);
    font-family: "Michroma", "Eurostile", sans-serif;
    position: relative;
  }
  .card {
    position: absolute;
    left: 180px;
    width: 840px;
    height: 480px;
    border-radius: 4px;
    box-shadow: 0 14px 30px var(--shadow);
    overflow: hidden;
  }
  .card--back {
    top: 30px;
    background: var(--card-dark);
    color: var(--ink-light);
  }
  .card--front {
    top: 540px;
    background: var(--card-light);
    color: var(--ink-dark);
  }

  /* Back side */
  .brand-mark {
    position: absolute;
    left: 420px;
    top: 70px;
    display: flex;
    align-items: center;
    gap: 18px;
  }
  .brand-mark__dot {
    width: 44px;
    height: 44px;
    border-radius: 50%;
    background: var(--ink-light);
  }
  .brand-mark__name {
    font-size: 34px;
    letter-spacing: 4px;
    color: var(--ink-light);
  }
  .tagline {
    position: absolute;
    left: 0;
    right: 0;
    top: 300px;
    margin: 0;
    text-align: center;
    font-size: 21px;
    line-height: 34px;
    letter-spacing: 3px;
    text-transform: uppercase;
  }
  .tagline span {
    display: block;
  }
  .tagline span:first-child {
    padding-left: 110px;
  }

  /* Front side */
  .company-name {
    position: absolute;
    right: 60px;
    top: 52px;
    margin: 0;
    font-size: 30px;
    font-weight: 400;
    font-variant: small-caps;
    letter-spacing: 4px;
  }
  .sphere-art {
    position: absolute;
    left: 300px;
    top: 110px;
    width: 290px;
    height: 290px;
  }
  .phone {
    position: absolute;
    left: 60px;
    top: 400px;
    margin: 0;
    font-size: 28px;
    letter-spacing: 14px;
  }
</style>
</head>
<body>

  <section class="card card--back" aria-label="Card back">
    <div class="brand-mark">
      <span class="brand-mark__dot"></span>
      <span class="brand-mark__name">VERELTO</span>
    </div>
    <p class="tagline">
      <span>A curated experience</span>
      <span>All that is promised is clarity</span>
    </p>
  </section>

  <section class="card card--front" aria-label="Card front">
    <h1 class="company-name">Verelto Services</h1>
    <svg class="sphere-art" viewBox="0 0 290 290" role="img" aria-label="Rainbow sphere of interlaced coloured threads and dots">
      <defs>
        <radialGradient id="sphereTone" cx="50%" cy="45%" r="55%">
          <stop offset="0%" stop-color="#f1e6f5"/>
          <stop offset="55%" stop-color="#d7c2ea"/>
          <stop offset="80%" stop-color="#c9dcb0"/>
          <stop offset="100%" stop-color="#f4c98a"/>
        </radialGradient>
      </defs>
      <circle cx="145" cy="145" r="140" fill="url(#sphereTone)"/>
    </svg>
    <p class="phone">555-014-2290</p>
  </section>

</body>
</html>
```